ZolvantaRx -- Reshaping the Future

Redesign our B2B website using the current logo attached (zolvantarx-example.com).
Our company is based in New York.
ZolvantaRx is our company logo.
TWB logo represents our patent approved technology that serves our clients.
We are Affordability Program Administrators. Our clients are pharmaceutical manufacturers that sponsor affordability programs designed to attract consumers of their products (pharmaceutical medication) and prescribers (doctors that prescribe medication).
We oversee their programs by processing claims submitted by pharmacies and all sites of care for reimbursement (or rebates) on medication they purchased.
We want a new brand. We are open to changing the logo color.
See logos and an one-page overview attached.

Target Market(s)

pharmaceutical manufacturers

Industry/Entity Type

manufacturers of pharmaceuticals and other clinical products; life sciences

Number of Pages Required

5+ page

Font styles to use
Other font styles liked:
• Use the font used in the logo -- Cy. We currently use that with IBM Plex Sans. Open to changing IBM but keep CY.

Requirements
Must have
• Must appeal to pharmaceutical manufacturers; convey a level of sophistication; send a message of creativity and change
Nice to have
• simple -- easy to read messaging.
Should not have
• too many pictures of doctors or patients.

```html
<!DOCTYPE html>
<html lang="en">
<head>
<meta charset="utf-8">
<title>ZolvantaRx — Reshaping the Future</title>
<link href="https://fonts.googleapis.com/css2?family=Saira+Semi+Condensed:wght@500;600;700&family=Roboto:wght@400;500&display=swap" rel="stylesheet">
<style>
:root{
  --navy-deep:#0a0f2e;
  --navy:#1b2778;
  --navy-text:#1e2b82;
  --lime:#c6d41a;
  --lime-soft:#8f9a10;
  --white:#ffffff;
  --panel:#000000;
  --btn:linear-gradient(90deg,#1b2778 0%,#2a3a86 40%,#c9d81c 100%);
}
*{margin:0;padding:0;box-sizing:border-box}
html,body{width:1200px;height:3104px;overflow:hidden}
body{position:relative;font-family:'Roboto',sans-serif;color:var(--white);background:var(--white)}
.display{font-family:'Saira Semi Condensed',sans-serif;font-weight:600}
.abs{position:absolute}
.btn{position:absolute;display:flex;align-items:center;justify-content:center;background:var(--btn);color:var(--white);font-family:'Roboto',sans-serif;font-weight:500;border-radius:10px;text-decoration:none}

.dark-band{position:absolute;left:0;top:0;width:1200px;height:1448px;
  background:
    radial-gradient(ellipse 420px 260px at 150px 170px,rgba(140,150,10,.75),transparent 70%),
    radial-gradient(ellipse 380px 300px at 1000px 360px,rgba(150,160,15,.7),transparent 70%),
    radial-gradient(ellipse 500px 300px at 700px 60px,rgba(110,120,10,.55),transparent 70%),
    radial-gradient(ellipse 600px 360px at 200px 1200px,rgba(120,130,10,.55),transparent 70%),
    radial-gradient(ellipse 500px 360px at 1050px 1100px,rgba(120,130,10,.5),transparent 70%),
    var(--navy-deep);}
.brand-name{font-family:'Saira Semi Condensed',sans-serif;font-weight:600;color:var(--white);white-space:nowrap}
.nav{position:absolute;top:28px;left:432px;display:flex;gap:25px;font-size:12px}
.nav span{color:var(--white)}
.hero-title{position:absolute;left:0;width:1200px;text-align:center;line-height:1}

.platform-panel{position:absolute;left:112px;top:657px;width:976px;height:232px;background:var(--panel);border:1px solid var(--lime-soft);border-radius:12px}
.platform{position:absolute;top:0;width:310px;text-align:center}
.platform .mark{height:150px;display:flex;align-items:center;justify-content:center;font-family:'Saira Semi Condensed',sans-serif;font-weight:600;font-size:42px;white-space:nowrap}
.platform p{font-size:11.5px;line-height:18px;color:var(--white)}

.psp-title{position:absolute;top:945px;left:0;width:1200px;text-align:center;font-size:31px}
.psp-card{position:absolute;top:1019px;width:188px;height:177px;border:1px solid var(--lime-soft);border-radius:8px;
  background:radial-gradient(circle at 50% 45%,#7d8a08 0%,#2e3a0a 55%,#151d10 100%)}
.psp-text{position:absolute;top:1208px;width:178px;font-size:11.5px;line-height:19px;color:var(--white)}

.feature-img{position:absolute;width:408px;height:264px;border:2px solid var(--lime);border-radius:10px}
.feature-head{position:absolute;font-size:23px;line-height:30px;color:var(--navy-text);font-weight:500;font-family:'Saira Semi Condensed',sans-serif}

.cta-band{position:absolute;left:0;top:2489px;width:1200px;height:615px;
  background:
    radial-gradient(ellipse 420px 340px at 1020px 2850px,rgba(150,160,15,.75),transparent 70%),
    radial-gradient(ellipse 400px 260px at 160px 2580px,rgba(110,120,10,.45),transparent 70%),
    radial-gradient(ellipse 420px 300px at 600px 3100px,rgba(100,110,10,.4),transparent 70%),
    var(--navy-deep);}
.footer-col{position:absolute;top:2866px}
.footer-col h4{font-family:'Saira Semi Condensed',sans-serif;font-weight:600;font-size:22px;margin-bottom:14px}
.footer-col li{list-style:none;font-size:11.5px;line-height:30px}
.contact-row{display:flex;align-items:center;gap:8px;font-size:11.5px;height:38px}
.contact-icon{width:28px;height:28px;border-radius:50%;background:#000;display:flex;align-items:center;justify-content:center}
</style>
</head>
<body>

<section class="dark-band">
  <div class="brand-name abs" style="left:123px;top:62px;font-size:27px">ZolvantaRx</div>
  <nav class="nav">
    <span>Home</span><span>Our Platforms</span><span>Payor Solutions</span><span>Pharmacy Solutions</span><span>About Us</span><span>Discovery</span>
  </nav>
  <a class="btn" style="left:965px;top:17px;width:113px;height:38px;font-size:14px;border-radius:6px">Let’s Talk</a>

  <h1 class="hero-title display" style="top:258px;font-size:76px">ZolvantaRx</h1>
  <h2 class="hero-title display" style="top:340px;font-size:82px;font-weight:700">Reshaping the Future</h2>
  <a class="btn" style="left:505px;top:448px;width:197px;height:59px;font-size:18px">Get Started</a>

  <div class="platform-panel">
    <div class="platform" style="left:30px">
      <div class="mark" style="font-size:30px">Zolvanta Brand Loyalty</div>
      <p>A NEW affordability platform and market<br>access solutionfor manufacturers</p>
    </div>
    <div class="platform" style="left:333px">
      <div class="mark" style="font-size:64px">TWB</div>
      <p>The power of infinite technology to maximize<br>access toyour brand across the life cycle</p>
    </div>
    <div class="platform" style="left:628px;width:340px">
      <div class="mark">ZVX Check</div>
      <p>An integrated pharmacy solution for electronic<br>eligibility verification and real-time prescription benefits</p>
    </div>
  </div>

  <h3 class="psp-title display">We’re changing the future of Patient Service Programs (PSP)</h3>

  <div class="psp-card" style="left:112px" role="img" aria-label="Glowing circuit-board brain"></div>
  <div class="psp-card" style="left:309px" role="img" aria-label="Abstract glowing circuit lines"></div>
  <div class="psp-card" style="left:506px" role="img" aria-label="Digital head made of particles"></div>
  <div class="psp-card" style="left:703px" role="img" aria-label="Digital globe with light points"></div>
  <div class="psp-card" style="left:900px" role="img" aria-label="Glowing microchip core"></div>

  <p class="psp-text" style="left:121px">PSP sponsored by manufacturers of pharmaceutical drugs, devices, diagnostics, and other clinical products.</p>
  <p class="psp-text" style="left:314px">A business built around imagining what progressive, efficient, and cost-effective patient services looks like.</p>
  <p class="psp-text" style="left:514px">Making drugs affordable and accessible by simplifying the process.</p>
  <p class="psp-text" style="left:711px">Our platforms and our values will bring your brand to life in the marketplace, reshaping the patient experience.</p>
  <p class="psp-text" style="left:906px">Market access solutions for manufacturers to serve patients in all sites of care</p>

  <a class="btn" style="left:457px;top:1312px;width:285px;height:60px;font-size:18px">Patient Service Programs</a>
</section>

<main>
  <div class="feature-img" style="left:183px;top:1513px;background:linear-gradient(180deg,#2c3a9a 0%,#22318a 70%,#c9cde0 100%)" role="img" aria-label="Ladder rising from clouds in a blue room"></div>
  <div class="feature-img" style="left:608px;top:1513px;background:linear-gradient(135deg,#5aa8e8,#3b86d6)" role="img" aria-label="Silver key on blue puzzle pieces"></div>
  <h3 class="feature-head" style="left:189px;top:1783px;width:390px">Take control of affordability, access, and adherence...</h3>
  <h3 class="feature-head" style="left:611px;top:1787px;width:420px">Identify market access andaffordability strategies for all sites of care</h3>
  <a class="btn" style="left:189px;top:1862px;width:167px;height:60px;font-size:18px">Take Control</a>
  <a class="btn" style="left:611px;top:1862px;width:167px;height:60px;font-size:18px">Market Access</a>

  <div class="feature-img" style="left:183px;top:1958px;background:linear-gradient(90deg,#e6f046 0%,#e6f046 14%,#f4f4f8 14%,#ffffff 100%)" role="img" aria-label="Tablet showing a claims utilization report screen"></div>
  <div class="feature-img" style="left:608px;top:1958px;background:linear-gradient(180deg,#5fc4c0 0%,#72b8c8 60%,#8f9ed6 100%)" role="img" aria-label="Small houses with location pins"></div>
  <h3 class="feature-head" style="left:189px;top:2227px;width:370px">Secure your competitive edge with advanced remittance solutions, transparency, and robust data-driven reporting</h3>
  <h3 class="feature-head" style="left:611px;top:2231px;width:400px">Mobilize delivery of care through provider networks, communication, fulfillment, and patient resources</h3>
  <a class="btn" style="left:189px;top:2357px;width:198px;height:60px;font-size:18px">Secure your edge</a>
  <a class="btn" style="left:611px;top:2334px;width:178px;height:60px;font-size:18px">Mobilize delivery</a>
</main>

<footer class="cta-band">
  <h2 class="display abs" style="left:0;top:92px;width:1200px;text-align:center;font-size:52px;line-height:52px">Connect with the power behind technologically<br>driven program optimization</h2>
  <a class="btn" style="left:510px;top:234px;width:178px;height:60px;font-size:18px">Connect</a>

  <div class="brand-name abs" style="left:123px;top:420px;font-size:27px">ZolvantaRx</div>
  <div class="abs" style="left:123px;top:470px;width:26px;height:26px;border-radius:50%;background:#000" aria-label="Social profile"></div>
  <p class="abs" style="left:123px;top:512px;font-size:11.5px">Privacy Policy</p>
  <p class="abs" style="left:123px;top:542px;font-size:11.5px">©2022 ZolvantaRx LLC. All rights reserved.</p>
</footer>

<div class="footer-col" style="left:365px">
  <h4>Home</h4>
  <ul><li>Our Platforms</li><li>Payor Solutions</li><li>Pharmacy Solutions</li><li>About Us</li><li>Discovery</li></ul>
</div>
<div class="footer-col" style="left:591px">
  <h4>Our Platforms</h4>
  <ul><li>Payor Solutions</li><li>Zolvanta Brand Loyalty®</li><li>ZolvantaRx Claims Processor®</li><li>Pharmacy Solutions</li><li>ZVX Check</li></ul>
</div>
<div class="footer-col" style="left:853px">
  <h4>Contact Us</h4>
  <div class="contact-row"><span class="contact-icon"><svg width="10" height="14" viewBox="0 0 10 14"><rect x="1" y="1" width="8" height="12" rx="1.5" fill="none" stroke="#fff" stroke-width="1.4"/></svg></span>555-014-2290</div>
  <div class="contact-row"><span class="contact-icon"><svg width="12" height="9" viewBox="0 0 12 9"><rect x="0.5" y="0.5" width="11" height="8" fill="#fff"/><path d="M0.5 0.5 6 5 11.5 0.5" fill="none" stroke="#000"/></svg></span>info@zolvantarx-example.com</div>
</div>

</body>
</html>
```